The homepage of a website

This is a simple project that should take from you a few minutes as what is needed is the design of the homepage only, the details are in the attached zip file

Please note that KBLTA board required a special tailored design where they got some parts from the different posted designs, if you are interested please follow the instructions in the below URL and submit your new updated designs as per the instructions (P.S. I will mark the project as guaranteed as an assurance to all of you)

http://quorvanet.com/Projects/KBLTA/Design.jpg

Please note that KBLTA board required a special tailored design where they got some parts from the different posted designs, if you are interested please follow the instructions in the below URL and submit your new updated designs as per the instructions (P.S. I will mark the project as guaranteed as an assurance to all of you) http://quorvanet.com/Projects/KBLTA/Design.jpg

```html
<!DOCTYPE html>
<html lang="en">
<head>
<meta charset="utf-8">
<title>KBLTA – Home</title>
<link rel="stylesheet" href="https://fonts.googleapis.com/css2?family=Lato:wght@400;700&family=Raleway:wght@500;600;700&display=swap">
<style>
:root{
  --navy:#0d3a68;
  --navy-dark:#0a2f66;
  --navy-deep:#081f47;
  --orange:#f26522;
  --cal-orange:#f26b3a;
  --blue:#1a6fb5;
  --grey-band:#e3e3e3;
  --top-grey:#dcdcdc;
  --text:#333;
  --muted:#666;
  --white:#fff;
}
*{box-sizing:border-box;margin:0;padding:0}
html,body{width:1200px;height:2566px;overflow:hidden}
body{font-family:"Lato",Arial,sans-serif;color:var(--text);background:var(--white);font-size:14px}
.wrap{width:952px;margin-left:124px;position:relative}
section,header,footer,nav{position:relative}

/* top bar */
.topbar{height:48px;background:var(--top-grey)}
.topbar .wrap{display:flex;align-items:center;height:48px}
.lang{width:80px;height:28px;background:var(--blue);color:#fff;font-size:12px;padding:6px 8px;display:flex;justify-content:space-between}
.search{margin-left:12px;width:164px;height:28px;background:#fff;border:1px solid #ccc;font-size:11px;color:#999;padding:7px 8px}
.search-btn{width:30px;height:28px;background:var(--blue);display:flex;align-items:center;justify-content:center}
.auth{margin-left:auto;display:flex;gap:22px}
.auth span{display:block;width:77px;height:28px;background:var(--blue);color:#fff;font-weight:700;font-size:13px;text-align:center;line-height:28px;border:1px solid #0f4f88}

/* header */
.masthead{height:138px;background:#fff}
.masthead .wrap{display:flex;align-items:center;height:138px}
.brand-mark{display:flex;align-items:center;gap:12px}
.brand-mark i{display:block;width:64px;height:64px;border-radius:50%;background:var(--navy)}
.brand-mark b{font-family:"Raleway",sans-serif;font-size:26px;color:var(--navy);font-weight:700}
.society-name{margin-left:auto;font-family:"Raleway",sans-serif;font-size:26px;font-weight:600;color:var(--navy);text-align:right;line-height:1.35}

/* nav */
.mainnav{height:50px;background:linear-gradient(#1b5c93,var(--navy))}
.mainnav ul{list-style:none;display:flex;height:50px;border-left:1px solid #0a2c50}
.mainnav li{color:#fff;font-size:15px;line-height:50px;padding:0 26px;border-right:1px solid #0a2c50}

/* hero */
.hero{height:579px;background:linear-gradient(120deg,#b9dbe8 0%,#7fb3cf 35%,#4f86b3 60%,#9cc6da 100%)}
.hero-caption{position:absolute;left:98px;top:207px;width:769px;height:166px;background:rgba(40,70,100,.62);padding:34px 26px}
.hero-caption h1{font-family:"Raleway",sans-serif;color:#fff;font-weight:600;font-size:40px;line-height:1.45}

/* welcome */
.welcome{height:306px}
.welcome .wrap{padding-top:20px;display:flex}
.welcome-text{width:462px}
.sec-title{font-family:"Lato",sans-serif;font-weight:700;font-size:26px;color:var(--orange)}
.sec-title span{color:var(--navy)}
.welcome-text p{font-size:12.5px;line-height:1.72;margin-top:10px}
.btn{display:inline-block;background:var(--navy);color:#fff;font-size:13px;padding:7px 14px;border-bottom:3px solid #061e3a;margin-top:18px}
.poster{margin-left:26px;margin-top:5px;width:219px;height:241px;background:linear-gradient(160deg,#f3efe6,#e9d6b8 55%,#7aa1c4)}
.calendar{margin-left:26px;width:219px}
.calendar h3{font-size:20px;color:var(--navy);font-weight:700;letter-spacing:.5px}
.calendar h3 span{color:var(--orange)}
.cal{margin-top:6px;background:var(--cal-orange);color:#fff}
.cal-head{height:28px;display:flex;align-items:center;justify-content:space-between;padding:0 8px;font-size:15px}
.cal-head i{width:16px;height:16px;border-radius:50%;background:#fff;display:block}
.cal table{width:100%;border-collapse:collapse;text-align:center;font-size:13px}
.cal th{background:var(--navy);font-weight:400;font-size:12px;height:22px}
.cal td{height:22px}

/* features */
.features{height:246px;background:var(--grey-band)}
.feature{position:absolute;top:31px;width:300px;text-align:center}
.feature .icon{width:80px;height:80px;border-radius:50%;background:var(--navy);margin:0 auto;display:flex;align-items:center;justify-content:center}
.feature h4{font-family:"Lato",sans-serif;font-size:21px;color:var(--navy);margin-top:14px;letter-spacing:.5px}
.feature p{font-size:13px;color:var(--muted);line-height:1.6;margin-top:4px;letter-spacing:.3px}

/* gallery */
.gallery{height:298px}
.gallery .wrap{padding-top:18px}
.gallery-row{display:flex;gap:25px;margin-top:22px}
.shot{width:219px;height:153px}
.arrows{display:flex;justify-content:center;gap:18px;margin-top:17px}
.arrows i{display:flex;width:31px;height:31px;border-radius:50%;background:var(--orange);align-items:center;justify-content:center}

/* news */
.news{height:369px;background:var(--grey-band)}
.news-col{position:absolute;top:20px;width:300px}
.item{display:flex;gap:12px;margin-top:17px}
.item:first-of-type{margin-top:20px}
.thumb{width:138px;height:117px;flex:none}
.item h5{color:var(--orange);font-size:13px;line-height:1.6}
.item p{font-size:13px;line-height:1.6}
.journal h5{color:var(--orange);font-size:19px;font-weight:400;margin-top:20px}
.journal small{display:block;font-size:12px;font-weight:700}
.journal p{font-size:12.5px;line-height:1.75;margin-top:10px}

/* partners */
.partners{height:185px}
.partners .wrap{padding-top:20px}
.partner-row{display:flex;gap:23px;margin-top:18px}
.badge{width:172px;height:81px;border:2px solid var(--navy);display:flex;align-items:center;justify-content:center}
.badge i{display:block;width:46px;height:46px;border-radius:50%;border:3px solid var(--navy)}

/* footer */
.site-footer{height:295px;background:var(--navy-dark);color:#fff}
.fcol{position:absolute;top:30px}
.fcol h6{font-size:16px;font-weight:700;padding-bottom:6px;border-bottom:1px solid #fff}
.links{list-style:none;position:absolute;top:72px;font-size:13px}
.links li{height:21.4px}
.links li::before{content:"» ";}
.newsletter p{font-size:11.5px;line-height:1.6;margin-top:10px;width:190px}
.field{width:180px;height:24px;background:#fff;color:#999;font-size:11px;padding:5px 6px;margin-top:8px}
.subscribe{display:inline-block;background:#1d5c9a;font-size:12px;padding:5px 14px;margin-top:14px}
.social{display:flex;align-items:center;gap:24px;margin-top:12px;font-weight:700;font-size:15px}
.social:first-of-type{margin-top:14px}
.social i{width:44px;height:44px;background:#1d5c9a;display:block}
.copyright{height:52px;background:var(--navy-deep);color:#fff;text-align:center;font-size:13px;line-height:52px}
</style>
</head>
<body>

<div class="topbar"><div class="wrap">
  <div class="lang">English <span>▾</span></div>
  <div class="search">Search Here</div>
  <div class="search-btn"><svg width="14" height="14" viewBox="0 0 14 14"><circle cx="6" cy="6" r="4.2" fill="none" stroke="#fff" stroke-width="2"/><line x1="9" y1="9" x2="13" y2="13" stroke="#fff" stroke-width="2"/></svg></div>
  <div class="auth"><span>Login</span><span>Register</span></div>
</div></div>

<header class="masthead"><div class="wrap">
  <div class="brand-mark"><i></i><b>KBLTA</b></div>
  <div class="society-name">The Delta Society Of Plastic<br>&amp; Reconstructive Surgeons</div>
</div></header>

<nav class="mainnav"><div class="wrap"><ul>
  <li>Home</li><li>Board</li><li>History</li><li>Members</li><li>Activities</li><li>Laws</li><li>Journal</li><li>Downloads</li><li>Links</li><li>Contact</li>
</ul></div></nav>

<section class="hero" role="img" aria-label="Surgical team in scrubs operating in a bright operating theatre">
  <div class="hero-caption"><h1>The Delta Society of Plastic And Reconstructive Surgeons</h1></div>
</section>

<section class="welcome"><div class="wrap">
  <div class="welcome-text">
    <h2 class="sec-title">Welcome To <span>KBLTA</span></h2>
    <p>There are many variations of passages of Lorem Ipsum available, but the majority have suffered alteration in some form, by injected humour, or randomised words which don't look even slightly believable. If you are going to use a passage of Lorem Ipsum, you need to be sure there isn't anything embarrassing hidden in the middle of text. All the Lorem Ipsum generators on the Internet tend to repeat predefined chunks as necessary, making this the first true generator on the Internet. It uses a dictionary of over 200 Latin words, combined with a handful of model sentence characteristic words etc.</p>
    <span class="btn">READ MORE</span>
  </div>
  <div class="poster" role="img" aria-label="Annual meeting 2014 conference poster"></div>
  <div class="calendar">
    <h3>EVENT'S <span>CALENDER</span></h3>
    <div class="cal">
      <div class="cal-head"><i></i><span>January 2015</span><i></i></div>
      <table>
        <tr><th>MON</th><th>TUE</th><th>WED</th><th>THU</th><th>FRI</th><th>SAT</th><th>SUN</th></tr>
        <tr><td>1</td><td>2</td><td>3</td><td>4</td><td>5</td><td>6</td><td>7</td></tr>
        <tr><td>5</td><td>6</td><td>7</td><td>8</td><td>9</td><td>10</td><td>11</td></tr>
        <tr><td>12</td><td>13</td><td>14</td><td>15</td><td>16</td><td>17</td><td>18</td></tr>
        <tr><td>19</td><td>19</td><td>20</td><td>21</td><td>22</td><td>23</td><td>24</td></tr>
        <tr><td>25</td><td>26</td><td>27</td><td>28</td><td>29</td><td>30</td><td></td></tr>
      </table>
    </div>
  </div>
</div></section>

<section class="features">
  <div class="feature" style="left:124px">
    <div class="icon"><svg width="40" height="40" viewBox="0 0 40 40" fill="#fff"><polygon points="20,4 37,13 3,13"/><rect x="6" y="15" width="4" height="15"/><rect x="14" y="15" width="4" height="15"/><rect x="22" y="15" width="4" height="15"/><rect x="30" y="15" width="4" height="15"/><rect x="3" y="32" width="34" height="4"/></svg></div>
    <h4>University</h4>
    <p>There are many variations of passages of Lorem Ipsum available, but the majority have suffered alteration in some form,</p>
  </div>
  <div class="feature" style="left:448px">
    <div class="icon"><svg width="44" height="44" viewBox="0 0 44 44" fill="none" stroke="#fff" stroke-width="3"><circle cx="22" cy="22" r="17"/><polygon points="22,12 36,18 22,24 8,18" fill="#fff" stroke="none"/><path d="M14 21v6c4 3 12 3 16 0v-6"/></svg></div>
    <h4>E-Learning</h4>
    <p>There are many variations of passages of Lorem Ipsum available, but the majority have suffered alteration in some form,</p>
  </div>
  <div class="feature" style="left:776px">
    <div class="icon"><svg width="44" height="44" viewBox="0 0 44 44" fill="none" stroke="#fff" stroke-width="3"><path d="M10 6v10a8 8 0 0 0 16 0V6"/><path d="M18 24v6a8 8 0 0 0 16 0v-6"/><circle cx="34" cy="20" r="4"/></svg></div>
    <h4>Petients Educations</h4>
    <p>There are many variations of passages of Lorem Ipsum available, but the majority have suffered alteration in some form,</p>
  </div>
</section>

<section class="gallery"><div class="wrap">
  <h2 class="sec-title">Our <span>Gallery</span></h2>
  <div class="gallery-row">
    <div class="shot" role="img" aria-label="Surgeon in scrubs in an operating room" style="background:linear-gradient(135deg,#6fb7a8,#3f7f74)"></div>
    <div class="shot" role="img" aria-label="Patient receiving a cosmetic consultation" style="background:linear-gradient(135deg,#e8eef2,#c9a68f)"></div>
    <div class="shot" role="img" aria-label="Doctors in white coats reviewing notes" style="background:linear-gradient(135deg,#eef2f4,#a9c2d4)"></div>
    <div class="shot" role="img" aria-label="Surgical team at work under blue light" style="background:linear-gradient(135deg,#3d6f9c,#9cc0dc)"></div>
  </div>
  <div class="arrows">
    <i><svg width="14" height="12" viewBox="0 0 14 12" fill="none" stroke="#fff" stroke-width="2"><path d="M7 1L2 6l5 5M12 1L7 6l5 5"/></svg></i>
    <i><svg width="14" height="12" viewBox="0 0 14 12" fill="none" stroke="#fff" stroke-width="2"><path d="M2 1l5 5-5 5M7 1l5 5-5 5"/></svg></i>
  </div>
</div></section>

<section class="news">
  <div class="news-col" style="left:124px">
    <h2 class="sec-title">Latest <span>News</span></h2>
    <div class="item"><div class="thumb" role="img" aria-label="Surgical instruments on a tray" style="background:linear-gradient(135deg,#cfe0ee,#7fa5c8)"></div><div><h5>Lorem Ipsum is simply dummy text of</h5><p>06.09.2014</p><p>Lorem Ipsum is simply dummy text of the printing and typesetting industry.</p></div></div>
    <div class="item"><div class="thumb" role="img" aria-label="Operating theatre with team" style="background:linear-gradient(135deg,#dfe9ef,#8fb0c6)"></div><div><h5>Lorem Ipsum is simply dummy text of</h5><p>06.09.2014</p><p>Lorem Ipsum is simply dummy text of the printing and typesetting industry.</p></div></div>
  </div>
  <div class="news-col" style="left:450px">
    <h2 class="sec-title">Upcoming <span>Events</span></h2>
    <div class="item"><div class="thumb" role="img" aria-label="Close view of surgical tools" style="background:linear-gradient(135deg,#4a5560,#9aa7b0)"></div><div><h5>Lorem Ipsum is simply dummy text of</h5><p>06.09.2014</p><p>Lorem Ipsum is simply dummy text of the printing and typesetting industry.</p></div></div>
    <div class="item"><div class="thumb" role="img" aria-label="Surgeons during an operation" style="background:linear-gradient(135deg,#2f5f80,#7fa8c0)"></div><div><h5>Lorem Ipsum is simply dummy text of</h5><p>06.09.2014</p><p>Lorem Ipsum is simply dummy text of the printing and typesetting industry.</p></div></div>
  </div>
  <div class="news-col journal" style="left:776px">
    <h2 class="sec-title"><span style="color:var(--orange)">KBLTA</span> <span>Journal</span></h2>
    <h5>Publishing Information</h5>
    <small>Powered By Dec 2014</small>
    <p>There are many variations of passages of Lorem Ipsum available, but the majority have suffered alteration in some form, by injected humour, or randomised words which don't look even slightly believable. If you are going to use a passage of Lorem Ipsum, you need to be sure there isn't anything embarrassing hidden in the middle of text. All the Lorem Ipsum generators on the Internet tend to repeat predefined chunks</p>
    <span class="btn" style="margin-top:14px">READ MORE</span>
  </div>
</section>

<section class="partners"><div class="wrap">
  <h2 class="sec-title">Our <span>Patners</span></h2>
  <div class="partner-row">
    <div class="badge"><i></i></div><div class="badge"><i></i></div><div class="badge"><i></i></div><div class="badge"><i></i></div><div class="badge"><i></i></div>
  </div>
</div></section>

<footer class="site-footer">
  <div class="fcol" style="left:124px;width:288px"><h6>Quick links</h6></div>
  <ul class="links" style="left:124px"><li>Home</li><li>Board</li><li>History</li><li>Members</li><li>Activities</li><li>Laws</li><li>Journal</li><li>Downloads</li><li>Links</li><li>Contact</li></ul>
  <ul class="links" style="left:288px"><li>Home</li><li>Board</li><li>History</li><li>Members</li><li>Activities</li><li>Laws</li><li>Journal</li><li>Downloads</li><li>Links</li><li>Contact</li></ul>
  <ul class="links" style="left:450px"><li>Home</li><li>Board</li><li>History</li><li>Members</li><li>Activities</li><li>Laws</li><li>Journal</li><li>Downloads</li><li>Links</li><li>Contact</li></ul>
  <div class="fcol newsletter" style="left:612px;width:190px">
    <h6>Newslatter</h6>
    <p>It is a long established fact that a reader will be distracted by the</p>
    <div class="field">Your Name</div>
    <div class="field">Your Email</div>
    <span class="subscribe">SUBSCIBE</span>
  </div>
  <div class="fcol" style="left:857px;width:188px">
    <h6>Follows Us</h6>
    <div class="social"><i></i>Friendbook</div>
    <div class="social"><i></i>Chirper</div>
    <div class="social"><i></i>Circles+</div>
    <div class="social"><i></i>ViewTube</div>
  </div>
</footer>
<div class="copyright">CopyRights © KBLTA 2015 By KBLTA.com All Rights Reserved</div>

</body>
</html>
```